K & D A/C Compressors' Business Card

Hello,

I need someone to create a new business card for my business. The name of my Business is: K & D A/C Compressors. I sell automotive air conditioning parts (a/c parts). I would like the business card to incorporate my logo, and to have an automotive feel to it. It is important that the business card feel like it is coming from an automotive parts business.

I already have a logo, which I will provide.

Thanks.
Updates

Project Deadline Extended Reason: I feel like extending the deadline until October 9, 2017, will allow for more time to design the business card. Thank you for your understanding. Added Monday, October 2, 2017

Target Market(s)

Consumers who need automotive a/c parts, and auto mechanics.

Industry/Entity Type

Automotive

Contact Information for Business Card

Business name: K & D A/C Compressors
Business Address: 48207 Southwest 36th Street, North Miami Beach, Florida 33162
Telephone: 305-472-1390
Fax: To be provided once I choose your design.
Website: www.kdcoolunits.example
Email: support@kdcoolunits.example
Names: To be provided once I choose your design.

Font styles to use
Sans Serif

Colors

Designer to choose colors to be used in the design.

Requirements
Must have
• The business card must include all of the "Business Card Details" and the logo I have uploaded.

```html
<!DOCTYPE html>
<html lang="en">
<head>
<meta charset="utf-8">
<title>K &amp; D A/C Compressors – Business Card</title>
<link rel="stylesheet" href="https://fonts.googleapis.com/css2?family=Roboto:ital,wght@0,300;0,400;0,700;0,900;1,900&display=swap">
<style>
  :root {
    --navy: #2e3192;
    --sky: #00aeef;
    --steel: #a7a9ac;
    --white: #ffffff;
    --backdrop: #e9eaec;
  }
  * { margin: 0; padding: 0; box-sizing: border-box; }
  html, body { width: 1200px; height: 960px; overflow: hidden; }
  body {
    background: var(--backdrop);
    font-family: "Roboto", Arial, sans-serif;
    display: flex;
    flex-direction: column;
    align-items: center;
    justify-content: center;
    gap: 56px;
  }
  .card {
    position: relative;
    width: 700px;
    height: 400px;
    overflow: hidden;
    box-shadow: 0 6px 18px rgba(0,0,0,.18);
  }

  /* Front: brand side */
  .card--brand {
    background: var(--navy);
    display: flex;
    align-items: center;
    justify-content: center;
  }
  .brand-name {
    color: var(--steel);
    font-weight: 300;
    font-size: 54px;
    letter-spacing: 1px;
    line-height: 1.1;
    text-align: center;
  }

  /* Back: contact side */
  .card--contact { background: var(--sky); }
  .card__band { position: absolute; inset: 0; width: 100%; height: 100%; }
  .person { position: absolute; left: 40px; top: 38px; }
  .person__name {
    color: var(--navy);
    font-weight: 900;
    font-style: italic;
    font-size: 28px;
    letter-spacing: -.5px;
    text-transform: uppercase;
  }
  .person__title { color: var(--white); font-size: 18px; font-weight: 400; margin-top: 2px; }

  .address {
    position: absolute;
    right: 40px;
    top: 238px;
    color: var(--white);
    font-size: 17px;
    line-height: 1.3;
    text-align: right;
  }
  .contact-list {
    position: absolute;
    left: 300px;
    top: 296px;
    list-style: none;
    color: var(--white);
    font-size: 16px;
    line-height: 1.35;
  }
  .contact-list li { display: flex; align-items: center; gap: 10px; }
  .contact-list svg { width: 14px; height: 14px; flex: none; fill: var(--sky); }
</style>
</head>
<body>

  <section class="card card--brand" aria-label="Card front">
    <p class="brand-name">K &amp; D<br>A/C Compressors</p>
  </section>

  <section class="card card--contact" aria-label="Card back">
    <svg class="card__band" viewBox="0 0 700 400" preserveAspectRatio="none" aria-hidden="true">
      <polygon fill="var(--navy)" points="0,190 700,220 700,400 0,400"/>
    </svg>

    <div class="person">
      <p class="person__name">Marcus Delaney</p>
      <p class="person__title">Managing Director</p>
    </div>

    <p class="address">48207 Southwest 36th Street<br>North Miami Beach, Florida 33162</p>

    <ul class="contact-list">
      <li>
        <svg viewBox="0 0 24 24" aria-hidden="true"><path d="M6.6 10.8a15 15 0 0 0 6.6 6.6l2.2-2.2a1 1 0 0 1 1-.25 11.4 11.4 0 0 0 3.6.57 1 1 0 0 1 1 1V20a1 1 0 0 1-1 1A17 17 0 0 1 3 4a1 1 0 0 1 1-1h3.5a1 1 0 0 1 1 1c0 1.25.2 2.45.57 3.57a1 1 0 0 1-.25 1z"/></svg>
        305-472-1390
      </li>
      <li>
        <svg viewBox="0 0 24 24" aria-hidden="true"><path d="M6 2h9l3 3v5H6zM3 11h18v9H3zm3 2v2h4v-2zm9 0v2h3v-2z"/></svg>
        305-472-1395
      </li>
      <li>
        <svg viewBox="0 0 24 24" aria-hidden="true"><path d="M2 21 23 12 2 3v7l15 2-15 2z"/></svg>
        support@kdcoolunits.example
      </li>
      <li>
        <svg viewBox="0 0 24 24" aria-hidden="true"><circle cx="12" cy="12" r="10"/></svg>
        www.kdcoolunits.example
      </li>
    </ul>
  </section>

</body>
</html>
```